Sports Nutrition Supplement Label design

We need a sports supplement label design for an existing business. (I have provided our business logo in the file uploads) These labels will remain consistent across the product line with the name of the product being the only changing field. The current product names (example: "vegan") on the labels provided are just for reference, the ingredients portions etc are final, but the actual name will be changed to something less generic for each product. I will just need to be able to change the name and have it match with label concept. We would like the look to be professional, clean, and exemplify quality. Please reference our business website kelvardathletic.com to get a feel for design and brand association.
I have also included the QVR supplement label guidelines so we are certain to maintain compliance.
Thank you and I'm looking forward to working with you and seeing your creative designs!
Doug
Updates

Target Market(s)

Athletes, Sports professionals, Colleges, Professional Sports Teams

Industry/Entity Type

Sports Science/ Sports Training/Athletics

Requirements
Nice to have
• I would like the design to possibly reflect these key terms: Sport Science, Chemistry, Clean, Professional, Quality (We also like water/ocean/waves concepts but is not a "requirement" it would have to really work well in the design somehow to appeal to wide range of athletes)

```html
<!DOCTYPE html>
<html lang="en">
<head>
<meta charset="utf-8">
<title>Kelvard Athletic – Chocolate Milkshake Label</title>
<link href="https://fonts.googleapis.com/css2?family=Open+Sans:wght@300;400;700&display=swap" rel="stylesheet">
<style>
  :root {
    --page: #ffffff;
    --ocean-deep: #1592c9;
    --ocean-light: #35b8e8;
    --lime: #7cc242;
    --lime-dark: #5fa52e;
    --band-edge: #2b2f33;
    --white: #ffffff;
    --cocoa-dark: #4a2c1c;
    --cocoa-mid: #6e4129;
    --cocoa-light: #8a5638;
  }
  * { margin: 0; padding: 0; box-sizing: border-box; }
  html, body {
    width: 1200px;
    height: 1200px;
    overflow: hidden;
    background: var(--page);
  }
  .canvas {
    position: relative;
    width: 1200px;
    height: 1200px;
  }
  .label {
    position: absolute;
    left: 100px;
    top: 165px;
    width: 1000px;
    height: 870px;
    overflow: hidden;
    background: radial-gradient(ellipse at 45% 45%, var(--ocean-light) 0%, var(--ocean-deep) 100%);
    font-family: "Open Sans", Arial, sans-serif;
    color: var(--white);
  }
  .band-top, .band-bottom {
    position: absolute;
    left: 0;
    width: 100%;
    background: var(--lime);
  }
  .band-top { top: 0; height: 20px; border-bottom: 3px solid var(--lime-dark); }
  .band-bottom { bottom: 0; height: 30px; border-top: 3px solid var(--lime-dark); }

  .flavor-splash {
    position: absolute;
    left: 330px;
    top: 300px;
    width: 720px;
    height: 250px;
    transform-origin: center;
    transform: translate(-20px, 140px) rotate(38deg);
    border-radius: 50% 40% 45% 55% / 60% 50% 50% 40%;
    background: radial-gradient(ellipse at 40% 45%, var(--cocoa-light) 0%, var(--cocoa-mid) 55%, var(--cocoa-dark) 100%);
    opacity: 0.92;
  }

  .brand {
    position: absolute;
    left: 242px;
    top: 96px;
    width: 520px;
    text-align: center;
    font-weight: 300;
    color: var(--white);
  }
  .brand-name {
    display: block;
    font-size: 150px;
    line-height: 1;
    letter-spacing: 12px;
  }
  .brand-tagline {
    display: block;
    margin-top: 18px;
    font-size: 36px;
    letter-spacing: 13px;
  }

  .line-tag {
    position: absolute;
    left: 258px;
    top: 400px;
    width: 100px;
    height: 440px;
  }
  .line-tag svg { display: block; }
  .line-tag-name {
    position: absolute;
    left: 50px;
    top: 275px;
    transform: translate(-50%, -50%) rotate(-90deg);
    font-size: 84px;
    font-weight: 700;
    letter-spacing: 2px;
    white-space: nowrap;
    color: var(--white);
  }

  .product-name {
    position: absolute;
    left: 392px;
    top: 488px;
    font-size: 52px;
    font-weight: 700;
    line-height: 72px;
  }
  .flavor-note {
    position: absolute;
    left: 392px;
    top: 664px;
    font-size: 40px;
    font-weight: 400;
  }
  .facts {
    position: absolute;
    left: 392px;
    top: 772px;
    font-size: 20px;
    font-weight: 400;
    line-height: 32px;
    text-transform: uppercase;
  }
</style>
</head>
<body>
<div class="canvas">
  <section class="label">
    <div class="band-top"></div>

    <div class="flavor-splash" role="img" aria-label="Chocolate milkshake splash illustration"></div>

    <div class="brand">
      <span class="brand-name">KELVARD</span>
      <span class="brand-tagline">ATHLETIC</span>
    </div>

    <div class="line-tag">
      <svg width="100" height="440" viewBox="0 0 100 440" aria-hidden="true">
        <polygon points="0,0 62,0 94,34 62,68 62,440 0,440" fill="var(--lime)"/>
        <polygon points="0,0 62,0 94,34 62,68 0,68" fill="var(--lime-dark)" opacity="0.35"/>
      </svg>
      <span class="line-tag-name">VEGAN</span>
    </div>

    <h1 class="product-name">CHOCOLATE<br>MILKSHAKE</h1>
    <p class="flavor-note">Natural Flavor</p>
    <p class="facts">Dietary Supplement<br>Net Wt.&nbsp; 907 G &nbsp;(2 LB)</p>

    <div class="band-bottom"></div>
  </section>
</div>
</body>
</html>
```